WordPress Site That Reviews Footwear

We need a wordpress web design for an affiliate site called TreadNest. We review and do roundups on footwear products. The final design should be clean and mobile friendly. The site should be built with Gutenberg page builder. We like the design of https://dermalquill.com/.
Updates

Need extra days to review

Target Market(s)

USA

Industry/Entity Type

Footwear

Logo Text

TreadNest

Number of Pages Required

4 page

Font styles to use
Serif
Sans Serif

Requirements
Must have
• Wordpress site
Blog post
Page
Categories
Homepage

```html
<!DOCTYPE html>
<html lang="en">
<head>
<meta charset="utf-8">
<title>TreadNest — Learn More About Shoes</title>
<link rel="stylesheet" href="https://fonts.googleapis.com/css2?family=Montserrat:wght@400;500;600;700;800;900&display=swap">
<style>
:root{
  --green:#05ff86;
  --yellow:#f9c846;
  --blue:#0a84ff;
  --ink:#0b0b0b;
  --footer:#0a1311;
  --white:#ffffff;
  --navy:#34465e;
}
*{margin:0;padding:0;box-sizing:border-box}
html,body{width:1200px;height:2427px;overflow:hidden;background:var(--white)}
body{position:relative;font-family:"Montserrat",sans-serif;color:var(--ink)}
.abs{position:absolute}

/* header */
.brand{left:151px;top:57px;color:var(--yellow);font-weight:900;font-size:24px;line-height:20px;text-transform:uppercase;letter-spacing:.5px}
.nav a{position:absolute;top:68px;font-size:18px;font-weight:400;color:var(--ink);text-decoration:none}
.menu-icon{left:1072px;top:70px}

/* hero */
.hero-title{left:154px;top:232px;font-weight:900;font-size:47px;line-height:48px}
.hero-sub{left:154px;top:342px;font-size:24px;line-height:24px;font-weight:400}
.btn-outline{display:flex;align-items:center;justify-content:center;border:3px solid var(--green);border-radius:20px;background:none;font-family:inherit;color:var(--ink)}
.hero-read{left:153px;top:430px;width:125px;height:38px;font-size:20px}
.hero-art{left:560px;top:130px;width:560px;height:500px}
.shoe-photo{left:585px;top:190px;width:480px;height:400px;border-radius:46% 38% 30% 42%/40% 30% 40% 50%;background:linear-gradient(160deg,#3b5574 0%,#2f6fb0 45%,#374558 70%,#f2f2f2 84%,#f6c72f 100%);transform:rotate(-18deg)}

/* blog */
.blog-title{left:0;width:1162px;top:668px;text-align:center;font-weight:900;font-size:45px}
.blog-rule{left:482px;top:733px;width:199px;height:6px;background:var(--ink);border-radius:3px}
.post{position:absolute;left:167px;width:640px;height:141px}
.post-thumb{position:absolute;left:0;top:0;width:141px;height:141px;border-radius:14px;background:var(--green);overflow:hidden}
.post-thumb span{position:absolute;left:-24px;top:26px;width:150px;height:84px;border-radius:40% 30% 30% 40%;transform:rotate(-18deg)}
.post-body{position:absolute;left:169px;top:11px;width:470px}
.post-title{font-weight:800;font-size:21px;line-height:24px}
.post-meta{font-size:13px;margin-top:1px;line-height:16px}
.post-text{font-size:12.6px;font-weight:500;line-height:15.7px;margin-top:12px}
.adverts{left:853px;top:859px;width:251px;height:985px;background:var(--green);border-radius:4px 4px 0 0;overflow:hidden}
.adverts-side{position:absolute;left:-8px;top:10px;color:var(--white);font-weight:900;font-size:30px;writing-mode:vertical-rl}
.adverts-foot{position:absolute;left:130px;top:966px;color:var(--white);font-weight:900;font-size:30px;white-space:nowrap}

/* footer */
.site-footer{left:0;top:1945px;width:1200px;height:482px;background:var(--footer);color:var(--white)}
.footer-brand{left:101px;top:75px;color:var(--yellow);font-weight:900;font-size:27px;line-height:24px;text-transform:uppercase}
.footer-about{left:101px;top:137px;width:260px;font-size:13px;line-height:15.5px;font-weight:500}
.footer-rule{left:101px;width:346px;height:3px;background:var(--white)}
.contact{left:101px;font-size:19px;font-weight:400}
.contact svg{vertical-align:-3px;margin-right:6px}
.socials{left:102px;top:397px;display:flex;gap:21px}
.socials span{width:24px;height:24px;border:2px solid var(--white);border-radius:50%}
.col-title{font-size:24px;font-weight:700}
.quick-title{left:504px;top:93px}
.quick-links{left:503px;top:131px;list-style:none}
.quick-links li{font-size:16px;height:29.3px;color:#e8e8e8}
.news-title{left:707px;top:93px;font-weight:900}
.email-field{left:707px;top:137px;width:393px;height:32px;background:var(--white);border-radius:5px;color:var(--ink);font-size:16px;padding:6px 16px}
.submit{left:707px;top:198px;width:125px;height:38px;font-size:20px;color:var(--white)}
</style>
</head>
<body>

<header>
  <div class="abs brand">Tread<br>Nest</div>
  <nav class="nav">
    <a style="left:683px">Home</a>
    <a style="left:816px;top:67px">Blog</a>
    <a style="left:936px">About</a>
  </nav>
  <svg class="abs menu-icon" width="20" height="18" viewBox="0 0 20 18" aria-label="Menu">
    <rect y="1" width="20" height="2" fill="#0b0b0b"/><rect y="8" width="20" height="2" fill="#0b0b0b"/><rect y="15" width="20" height="2" fill="#0b0b0b"/>
  </svg>
</header>

<section class="hero">
  <h1 class="abs hero-title">Learn More<br>About&nbsp; Shoes</h1>
  <p class="abs hero-sub">We review and do roundups<br>on footwear products</p>
  <a class="abs btn-outline hero-read">Read</a>

  <svg class="abs hero-art" width="560" height="500" viewBox="560 130 560 500">
    <path d="M866 188 A33 33 0 1 1 931 188" fill="none" stroke="#0a84ff" stroke-width="13"/>
    <circle cx="688" cy="391" r="42" fill="none" stroke="#05ff86" stroke-width="13"/>
    <circle cx="1052" cy="449" r="32" fill="none" stroke="#05ff86" stroke-width="13"/>
    <circle cx="902" cy="601" r="14" fill="#0a84ff"/>
  </svg>
  <div class="abs shoe-photo" role="img" aria-label="Photo of a navy and blue high-top sneaker with velcro strap and yellow sole"></div>
</section>

<section class="blog">
  <h2 class="abs blog-title">Blog</h2>
  <div class="abs blog-rule"></div>

  <article class="post" style="top:867px">
    <div class="post-thumb" role="img" aria-label="Blue high-top sneaker with yellow sole"><span style="background:linear-gradient(150deg,#3b5574,#2f6fb0 55%,#f2f2f2 85%,#f6c72f)"></span></div>
    <div class="post-body"><h3 class="post-title">Lorem Ipsum</h3><p class="post-meta">Content and stuff</p><p class="post-text">Lorem ipsum dolor sit amet, consectetur adipiscing elit, sed do eiusmod tempor incididunt ut labore et dolore magna aliqua. Quis ipsum suspendisse ultrices gravida. Risus commodo viverra maecenas accumsan lacus vel facilisis.</p></div>
  </article>
  <article class="post" style="top:1031px">
    <div class="post-thumb" role="img" aria-label="Pair of yellow and black basketball sneakers"><span style="background:linear-gradient(150deg,#1b1b1b,#f5cf10 50%,#1b1b1b 80%,#f2f2f2)"></span></div>
    <div class="post-body"><h3 class="post-title">Lorem Ipsum</h3><p class="post-meta">Content and stuff</p><p class="post-text">Lorem ipsum dolor sit amet, consectetur adipiscing elit, sed do eiusmod tempor incididunt ut labore et dolore magna aliqua. Quis ipsum suspendisse ultrices gravida. Risus commodo viverra maecenas accumsan lacus vel facilisis.</p></div>
  </article>
  <article class="post" style="top:1195px">
    <div class="post-thumb" role="img" aria-label="Black running shoe with red stripes"><span style="background:linear-gradient(150deg,#111,#2a2a2a 50%,#c0262b 70%,#f2f2f2)"></span></div>
    <div class="post-body"><h3 class="post-title">Lorem Ipsum</h3><p class="post-meta">Content and stuff</p><p class="post-text">Lorem ipsum dolor sit amet, consectetur adipiscing elit, sed do eiusmod tempor incididunt ut labore et dolore magna aliqua. Quis ipsum suspendisse ultrices gravida. Risus commodo viverra maecenas accumsan lacus vel facilisis.</p></div>
  </article>
  <article class="post" style="top:1360px">
    <div class="post-thumb" role="img" aria-label="Black and blue running shoe with neon accents"><span style="background:linear-gradient(150deg,#1d2a3a,#2664c4 50%,#b6e82a 75%,#1a1a1a)"></span></div>
    <div class="post-body"><h3 class="post-title">Lorem Ipsum</h3><p class="post-meta">Content and stuff</p><p class="post-text">Lorem ipsum dolor sit amet, consectetur adipiscing elit, sed do eiusmod tempor incididunt ut labore et dolore magna aliqua. Quis ipsum suspendisse ultrices gravida. Risus commodo viverra maecenas accumsan lacus vel facilisis.</p></div>
  </article>
  <article class="post" style="top:1524px">
    <div class="post-thumb" role="img" aria-label="Pair of white and burgundy court shoes"><span style="background:linear-gradient(150deg,#8c1748,#f4f4f4 50%,#8c1748 85%)"></span></div>
    <div class="post-body"><h3 class="post-title">Lorem Ipsum</h3><p class="post-meta">Content and stuff</p><p class="post-text">Lorem ipsum dolor sit amet, consectetur adipiscing elit, sed do eiusmod tempor incididunt ut labore et dolore magna aliqua. Quis ipsum suspendisse ultrices gravida. Risus commodo viverra maecenas accumsan lacus vel facilisis.</p></div>
  </article>
  <article class="post" style="top:1688px">
    <div class="post-thumb" role="img" aria-label="Blue high-top sneaker with yellow sole"><span style="background:linear-gradient(150deg,#3b5574,#2f6fb0 55%,#f2f2f2 85%,#f6c72f)"></span></div>
    <div class="post-body"><h3 class="post-title">Lorem Ipsum</h3><p class="post-meta">Content and stuff</p><p class="post-text">Lorem ipsum dolor sit amet, consectetur adipiscing elit, sed do eiusmod tempor incididunt ut labore et dolore magna aliqua. Quis ipsum suspendisse ultrices gravida. Risus commodo viverra maecenas accumsan lacus vel facilisis.</p></div>
  </article>

  <aside class="abs adverts">
    <span class="adverts-side">Adverts</span>
    <span class="adverts-foot">Adverts</span>
  </aside>
</section>

<footer class="abs site-footer">
  <div class="abs footer-brand">Tread<br>Nest</div>
  <p class="abs footer-about">Lorem ipsum dolor sit amet, consectetur adipiscing elit, sed do eiusmod tempor incididunt ut et</p>
  <div class="abs footer-rule" style="top:189px"></div>
  <div class="abs footer-rule" style="top:310px"></div>
  <p class="abs contact" style="top:326px">
    <svg width="18" height="18" viewBox="0 0 24 24"><path d="M6.6 10.8a15.1 15.1 0 0 0 6.6 6.6l2.2-2.2a1 1 0 0 1 1-.25 11.4 11.4 0 0 0 3.6.57 1 1 0 0 1 1 1V20a1 1 0 0 1-1 1A17 17 0 0 1 3 4a1 1 0 0 1 1-1h3.5a1 1 0 0 1 1 1c0 1.25.2 2.45.57 3.57a1 1 0 0 1-.25 1z" fill="#fff"/></svg>55-01-24-7788&nbsp;&nbsp;&nbsp;
    <svg width="18" height="18" viewBox="0 0 24 24"><path d="M6.6 10.8a15.1 15.1 0 0 0 6.6 6.6l2.2-2.2a1 1 0 0 1 1-.25 11.4 11.4 0 0 0 3.6.57 1 1 0 0 1 1 1V20a1 1 0 0 1-1 1A17 17 0 0 1 3 4a1 1 0 0 1 1-1h3.5a1 1 0 0 1 1 1c0 1.25.2 2.45.57 3.57a1 1 0 0 1-.25 1z" fill="#fff"/></svg>55-01-24-7788
  </p>
  <p class="abs contact" style="top:352px">hello@treadnest.co</p>
  <div class="abs socials" aria-label="Social links"><span></span><span></span><span></span><span></span></div>

  <h4 class="abs col-title quick-title">Quick Links</h4>
  <ul class="abs quick-links">
    <li>Home</li><li>Blog</li><li>About</li><li>Trending</li><li>Archives</li>
  </ul>

  <h4 class="abs col-title news-title">Subscribe to our Newsletter</h4>
  <div class="abs email-field">Enter Your Email Here</div>
  <a class="abs btn-outline submit">Submit</a>
</footer>

</body>
</html>
```